Business Card Design

I need a business card design for my new business based on Long Island, NY also serving NYC called Pine Hollow Kennel. I have built a website with printwell that can be looked at as a basis for the card. It is pinehollowkennel.example.

I board Labrador Retrievers in my home. Specialize in one breed. Cage free environment. Dogs have full run of home and fenced in property. Pine Hollow Kennel is a one-of-a-kind, high-quality dog-boarding provider serving specifically Labrador Retrievers. By working with a dog I am comfortable with, I am able to offer the best care for all pets that come through my door. I work with Lab owners in the Long Island/NYC area to provide an
in-home safe, reliable and fun environment for daycare and overnight stays.

I provide a unique boarding experience for Labrador Retrievers on Long Island. Your Lab should be well mannered, housebroken and good with other dogs. Provided your pet is well mannered and house trained, my boarding services allow dogs to experience a cage-free stay while having free roam of my home and property. This allows owners a unique alternative to a kennel, giving pets the chance to experience a home away from home rather than chain linked fences and cold concrete floors.
As a guest at Pine Hollow Kennel, your dog will get:

4-star kibble
Access to my in-ground pool
All-natural snack selection
Companionship of other retrievers including my two
Full run of entire home and fenced-in backyard
Photos AND videos posted to Chatterpage so you can see your dog having fun while away
Toys, bones and affection

I think it is important to have a pic of the 3 colored labs below. Also the picture of my own personal labs ..the white one with the black puppy. Maybe some paw prints. If using any imagery that MUST look EXACTLY like labrador retriever no generic dogs. Thank you
Updates

The Back of the Card should have the following: The background should be one of the pictures I sent (white dog in pool or another pic I included) At Pine Hollow Kennel your Lab gets: Cage Free Environment Full run of my home and fenced in yard In-ground pool Toys and affection Companionship of other Labrador Retrievers Photos and Videos posted Chatterpage of your loved one FRONT OF THE CARD: should include picture of the 3 labs (yellow white brown) OR picture of white dog in pool. Pine Hollow Kennel should be in larger font than the rest. the following can be in any order. Rick Dunmore Maple Ridge, NY in Central Long Island pinehollowkennel.example 631-555-0194

Industry/Entity Type

Environment

Contact Information for Business Card

Pine Hollow Kennel
Maple Ridge, NY
Rick Dunmore
pinehollowkennel@mailbox.example
631-555-0194

```html
<!DOCTYPE html>
<html lang="en">
<head>
<meta charset="utf-8">
<title>Pine Hollow Kennel – Business Card</title>
<link rel="stylesheet" href="https://fonts.googleapis.com/css2?family=Open+Sans:wght@300;400;600;700;800&display=swap">
<style>
  :root {
    --stage: #b9b3bb;
    --card-white: #ffffff;
    --ink: #1a1a1a;
    --tint: #f3eeee;
    --grass-light: #8fd14a;
    --grass-mid: #5fae2c;
    --grass-dark: #3d7d1c;
    --pup-cream: #e9d3ad;
    --pup-black: #2a2a2a;
    --pup-brown: #5a3a2c;
    --on-photo: #ffffff;
  }
  * { box-sizing: border-box; margin: 0; padding: 0; }
  html, body { width: 1200px; height: 800px; overflow: hidden; }
  body {
    background: var(--stage);
    font-family: "Open Sans", sans-serif;
    color: var(--ink);
  }
  .sheet {
    width: 1200px; height: 800px;
    display: flex; align-items: center; justify-content: center; gap: 50px;
  }
  .card {
    width: 540px; height: 310px;
    position: relative; overflow: hidden;
    box-shadow: 0 6px 18px rgba(0,0,0,0.18);
  }

  /* Contact side */
  .card--contact { background: var(--card-white); }
  .contact-pattern {
    position: absolute; inset: 0;
    background: linear-gradient(135deg, var(--card-white) 30%, var(--tint) 100%);
  }
  .contact-title {
    position: absolute; left: 30px; top: 22px;
    font-weight: 300; font-size: 32px; letter-spacing: 6px;
  }
  .contact-list {
    position: absolute; left: 24px; top: 86px;
    list-style: none; display: flex; flex-direction: column; gap: 7px;
  }
  .contact-item { display: flex; align-items: center; gap: 10px; font-size: 14px; }
  .contact-item--small { font-size: 11px; }
  .contact-name-small { font-size: 11px; }
  .contact-icon { width: 28px; height: 28px; flex: none; }
  .pups-photo {
    position: absolute; right: 24px; top: 120px;
    width: 230px; height: 170px;
    background: linear-gradient(100deg, var(--pup-cream) 0 33%, var(--pup-black) 33% 66%, var(--pup-brown) 66%);
    opacity: 0.85;
    border-radius: 6px;
  }

  /* Brand side */
  .card--brand {
    background: radial-gradient(ellipse at 40% 40%, var(--grass-light), var(--grass-mid) 55%, var(--grass-dark));
  }
  .brand-photo { position: absolute; inset: 0; }
  .brand-name {
    position: absolute; right: 26px; top: 26px;
    text-align: right; color: var(--on-photo);
    font-weight: 700; font-size: 46px; line-height: 1.05; text-transform: uppercase;
  }
  .brand-tagline {
    position: absolute; left: 26px; right: 26px; bottom: 34px;
    color: var(--on-photo); font-weight: 600; font-size: 21px;
    text-transform: uppercase; letter-spacing: 0.5px;
  }
</style>
</head>
<body>
<main class="sheet">
  <section class="card card--contact">
    <div class="contact-pattern" role="img" aria-label="Faint paw print pattern across the card"></div>
    <h2 class="contact-title">Contact :</h2>
    <ul class="contact-list">
      <li class="contact-item">
        <svg class="contact-icon" viewBox="0 0 28 28"><circle cx="14" cy="14" r="12.5" fill="none" stroke="#1a1a1a" stroke-width="1.5"/><path d="M14 6a5 5 0 0 0-5 5c0 4 5 10 5 10s5-6 5-10a5 5 0 0 0-5-5z" fill="#1a1a1a"/><circle cx="14" cy="11" r="1.8" fill="#fff"/></svg>
        <span><span class="contact-name-small">Pine Hollow Kennel</span><br>Maple Ridge, NY</span>
      </li>
      <li class="contact-item">
        <svg class="contact-icon" viewBox="0 0 28 28"><circle cx="14" cy="14" r="12.5" fill="none" stroke="#1a1a1a" stroke-width="1.5"/><circle cx="14" cy="10.5" r="4" fill="#1a1a1a"/><path d="M6.5 21c1-4 4-5.5 7.5-5.5s6.5 1.5 7.5 5.5z" fill="#1a1a1a"/></svg>
        <span>Rick Dunmore</span>
      </li>
      <li class="contact-item">
        <svg class="contact-icon" viewBox="0 0 28 28"><circle cx="14" cy="14" r="12.5" fill="none" stroke="#1a1a1a" stroke-width="1.5"/><path d="M10 7h3l1 4-2 1c1 2 2 3 4 4l1-2 4 1v3c-6 1-12-5-11-11z" fill="#1a1a1a"/></svg>
        <span>631-555-0194</span>
      </li>
      <li class="contact-item contact-item--small">
        <svg class="contact-icon" viewBox="0 0 28 28"><circle cx="14" cy="14" r="12.5" fill="none" stroke="#1a1a1a" stroke-width="1.5"/><rect x="7.5" y="9.5" width="13" height="9" fill="none" stroke="#1a1a1a" stroke-width="1.5"/><path d="M7.5 9.5l6.5 5 6.5-5" fill="none" stroke="#1a1a1a" stroke-width="1.5"/></svg>
        <span>pinehollowkennel@mailbox.example</span>
      </li>
      <li class="contact-item contact-item--small">
        <svg class="contact-icon" viewBox="0 0 28 28"><circle cx="14" cy="14" r="12.5" fill="none" stroke="#1a1a1a" stroke-width="1.5"/><rect x="9.5" y="7" width="9" height="14" rx="4.5" fill="none" stroke="#1a1a1a" stroke-width="1.5"/><line x1="14" y1="7" x2="14" y2="12" stroke="#1a1a1a" stroke-width="1.5"/></svg>
        <span>www.pinehollowkennel.example</span>
      </li>
    </ul>
    <div class="pups-photo" role="img" aria-label="Photo of three Labrador puppies: yellow, black and chocolate"></div>
  </section>

  <section class="card card--brand">
    <div class="brand-photo" role="img" aria-label="Photo of a yellow Labrador puppy sitting on green grass"></div>
    <h1 class="brand-name">Pine Hollow<br>Kennel</h1>
    <p class="brand-tagline">The best care for your best dog</p>
  </section>
</main>
</body>
</html>
```